Renewable Energy Consultancy needs relatively simple but smart website

We are a renewable energy focussed consultancy called Bellmoran, and we are just starting out. Our target is to bring knowledge of the detailed technical and commercial operations of renewables projects, mainly wind energy.

Our target customers are major energy utilities and private finance groups, who look to invest in renewables projects as a long term money-earning system. We are a fairly young, dynamic team of industry-respected people (4 of us) but we need to make ourselves look bigger than this (our customers will expect us to take on major projects, so we need to look big enough to handle it...)

We're not going to sell anything from our website and we expect it to just support our company name. Most of our customers are made by strong networks and relationships, so its mainly there to give confidence in our capabilities and give a strong view of who we are. We probably need a site with 4/5 pages which we can then expand when needed.

We have logos and headers (attached) which we want to use (also run through artpitchly), and I've attached a few pictures of projects similar to those we will be involved in to give us a feel for how it will look. Also attached are the colours we liked which are now used in the logo, and the font details. Whilst we're a "green" company with a "green" logo, we don't want to be completely green, so some nice combinations of colours on the pages would be good.

Ideally we need to have chirpnet/workgrid news feeds somewhere linked into the site.

The design should be smart - giving a feel of high integrity and assurance whilst making us seem approachable and knowledgeable.

Target Market(s)

Renewables investors, developers of renewables projects (wind farms etc),

Industry/Entity Type

Finance

Coding

Coded - Design and coding required

Number of Pages Required

4 page

Other font styles liked:
• See the attachment with brand text/colour details ("colour codes" filename)

Requirements
Must have
• A fairly simple, but smart website design. We're looking to provide confidence and consolidate our networks with the website, not specifically find new customers - so its really just to give customers somewhere they can relate to online
Nice to have
• We have logos/brands and colours - so a website which incorperates these well and brings accross a professional company
• Would be nice to have a page (such as a blog/wordpress) we can easily update with news/events etc and links to chirpnet feed and workgrid feed ideally.
Should not have
• cartoons, flashy gimmicks,

```html
<!DOCTYPE html>
<html lang="en">
<head>
<meta charset="utf-8">
<title>Bellmoran</title>
<link href="https://fonts.googleapis.com/css2?family=Open+Sans:wght@300;400;600;700&display=swap" rel="stylesheet">
<style>
:root{
  --green:#3f7a0d;
  --green-dark:#2f5f06;
  --green-light:#5a9a1c;
  --gold:#b7a51a;
  --ink:#333;
  --muted:#777;
  --pale:#ececec;
  --line:#dcdcdc;
  --white:#fff;
}
*{margin:0;padding:0;box-sizing:border-box}
html,body{width:780px;height:1200px;overflow:hidden;background:var(--white)}
body{position:relative;font-family:"Open Sans",Arial,sans-serif;color:var(--ink)}
.abs{position:absolute}
.top-rule{left:0;top:0;width:780px;height:2px;background:var(--green)}
.brand{display:flex;align-items:center;gap:8px}
.brand-dot{width:30px;height:30px;border-radius:50%;background:var(--green)}
.brand-name{font-weight:300;font-size:28px;color:#555;letter-spacing:.5px}
.social{display:flex;gap:4px}
.social span{width:18px;height:18px;background:#8a8a8a}
.btn{display:flex;align-items:center;justify-content:center;color:var(--white);font-size:10px;border-radius:2px}
.btn-green{background:var(--green);box-shadow:0 2px 0 var(--green-dark)}
.btn-grey{background:#8e8e8e;box-shadow:0 2px 0 #666}
.nav{left:39px;top:69px;width:702px;height:29px;background:linear-gradient(#4f8f12,#3a7209);display:flex}
.nav a{color:var(--white);font-size:9.5px;text-decoration:none;display:flex;align-items:center;padding:0 19px;height:100%;border-right:1px solid rgba(255,255,255,.12)}
.nav a.active{background:var(--green-dark);padding:0 19px}
.nav .login{margin-left:auto;background:var(--gold);padding:0 23px;border:none}
.hero{left:39px;top:108px;width:702px;height:323px;background:linear-gradient(#7fa6d2 0%,#a9c6e4 55%,#b9a98a 72%,#6d5f3f 100%)}
.arrow{width:24px;height:24px;border-radius:50%;background:rgba(255,255,255,.45)}
.cap-1{left:71px;top:339px;height:26px;padding:0 10px;background:rgba(255,255,255,.85);font-size:13px;line-height:26px;color:#333}
.cap-2{left:71px;top:371px;height:24px;padding:0 10px;background:rgba(63,122,13,.9);font-size:13px;line-height:24px;color:var(--white)}
.photo{background:linear-gradient(#9db8d6,#6c7f93 60%,#4b4f56)}
h2{font-weight:400;font-size:15px;color:#333}
p.body{font-size:7.6px;line-height:11px;color:#555}
.dots{display:flex;gap:4px}
.dots i{width:7px;height:7px;border-radius:50%;border:1px solid #999}
.dots i.on{background:var(--green);border-color:var(--green)}
.hot-item{left:561px;display:flex;gap:10px;width:170px}
.hot-item .thumb{width:43px;height:43px;flex:none}
.hot-item b{display:block;font-weight:400;font-size:8.8px;line-height:12px;color:#333}
.hot-item small{display:block;font-size:7.6px;color:#999;margin-top:5px}
.proj{width:156px;text-align:center}
.proj h3{font-weight:600;font-size:11.5px;color:#333;margin-bottom:10px}
.proj .frame{border:1px solid #e4e4e4;padding:4px;height:76px}
.proj .frame div{height:100%;background:linear-gradient(#3a5a7c,#1d3e66)}
.proj p{font-size:7.2px;line-height:12px;color:#555;margin-top:6px}
.invest{left:39px;top:829px;width:702px;height:110px;background:var(--pale);border-left:3px solid var(--green)}
.footer{left:0;top:989px;width:780px;height:171px;background:#ebebeb}
.foot-h{font-size:9px;font-weight:600;color:#444;top:1015px}
.links{list-style:none;font-size:7.8px;color:#666}
.links li{height:14px;display:flex;align-items:center;gap:8px}
.links li:before{content:"";width:4px;height:4px;border-radius:50%;background:#999}
.tile{width:9px;height:9px;background:#3a78b5}
.feed{background:var(--white);left:196px;top:1033px;width:119px;height:108px;padding:4px;font-size:5.2px;line-height:7px;color:#444}
.tweet{left:382px;width:150px;display:flex;gap:8px;font-size:6.6px;line-height:10px;color:#333}
.bird{width:18px;height:14px;background:#cfd8dc;border-radius:50%;flex:none}
.tweet em{font-style:normal;color:#6a8f9a}
.tweet .when{color:#c0241d}
.field{left:601px;width:137px;height:19px;background:var(--white);border:1px solid #e0e0e0;font-size:7.2px;color:#999;padding-left:6px;line-height:17px}
.bottom{left:0;top:1160px;width:780px;height:40px;background:var(--green)}
</style>
</head>
<body>
<div class="abs top-rule"></div>

<header>
  <div class="abs brand" style="left:39px;top:18px"><span class="brand-dot"></span><span class="brand-name">Bellmoran</span></div>
  <div class="abs social" style="left:529px;top:27px"><span></span><span></span><span></span><span></span></div>
  <a class="abs btn btn-green" style="left:621px;top:24px;width:117px;height:23px;font-size:10px;text-decoration:none">Invest With Us</a>
  <nav class="abs nav">
    <a class="active">HOME</a><a>PRODUCTS</a><a>SERVICES</a><a>WHY US?</a><a>COMPANY</a><a>CAREERS</a><a>CONTACT US</a>
    <a class="login">Login / Register</a>
  </nav>
</header>

<section class="abs hero" role="img" aria-label="Wind turbines standing in a harvested field with hay bales under a blue sky"></section>
<span class="abs arrow" style="left:50px;top:257px"></span>
<span class="abs arrow" style="left:704px;top:257px"></span>
<div class="abs cap-1">Lorem ipsum dolor sit amet</div>
<div class="abs cap-2">lacus velit, consectetur ac enim sed, euismod</div>

<section>
  <div class="abs photo" style="left:39px;top:463px;width:186px;height:126px" role="img" aria-label="Turbine installation vessel with crane in port"></div>
  <h2 class="abs" style="left:236px;top:458px">Welcome to Bellmoran</h2>
  <div class="abs" style="left:236px;top:482px;font-size:7px;font-style:italic;color:#5a7fa8">&#9711; Lorem ipsum</div>
  <p class="abs body" style="left:236px;top:499px;width:290px">Integer ornare libero nisi. Duis ac magna urna. Nulla facilisi. Phasellus at ante magna. Quisque nec porta nulla. Suspendisse nec orci vel elit aliquet blandit in non orci. Vivamus posuere dui eget lacinia rutrum. Cum sociis natoque penatibus et magnis dis parturient montes, nascetur ridiculus mus...</p>
  <a class="abs btn btn-green" style="left:236px;top:556px;width:59px;height:26px">Show More</a>
  <a class="abs btn btn-grey" style="left:302px;top:556px;width:83px;height:26px">Get Involved</a>
  <div class="abs" style="left:39px;top:599px;width:491px;height:2px;background:#ddd"></div>
</section>

<aside>
  <h2 class="abs" style="left:562px;top:459px">What’s Hot</h2>
  <div class="abs dots" style="left:689px;top:464px"><i class="on"></i><i></i><i></i></div>
  <div class="abs" style="left:550px;top:485px;width:180px;height:1px;background:var(--line)"></div>
  <div class="abs hot-item" style="top:497px"><div class="thumb photo" role="img" aria-label="Engineers on a wind site"></div><div><b>A Northlander doesn’t necessarily come from...</b><small>3 minutes ago</small></div></div>
  <div class="abs hot-item" style="top:551px"><div class="thumb photo" role="img" aria-label="Technician on solar panels"></div><div><b>A Northlander never looks up...</b><small>7 hours ago</small></div></div>
  <div class="abs hot-item" style="top:604px"><div class="thumb photo" role="img" aria-label="Turbine against blue sky"></div><div><b>A Northlander doesn’t take cabs</b><small>23 hours ago</small></div></div>
  <div class="abs hot-item" style="top:658px"><div class="thumb photo" role="img" aria-label="Solar array and turbines"></div><div><b>A Northlander views celebrities as regular...</b><small>1 day ago</small></div></div>
  <div class="abs hot-item" style="top:711px"><div class="thumb" style="background:linear-gradient(#6f9a3e,#8a6a4a)" role="img" aria-label="House roof with solar panels"></div><div><b>A Northlander never looks up...</b><small>2 days ago</small></div></div>
</aside>

<section>
  <h2 class="abs" style="left:40px;top:629px">Latest Projects</h2>
  <div class="abs dots" style="left:501px;top:639px"><i class="on"></i><i></i><i></i></div>
  <div class="abs proj" style="left:38px;top:667px"><h3>Nulla imperdiet</h3><div class="frame"><div role="img" aria-label="Offshore turbine foundation at sea"></div></div><p>Vitae adipiscing turpis. Aenean ligula nibh in, molestie id viverra a, dapibus at dolor.</p></div>
  <div class="abs proj" style="left:207px;top:667px"><h3>Integer aliquam</h3><div class="frame"><div style="background:linear-gradient(#6a6f78,#2e3038)" role="img" aria-label="Turbine blades loaded on vessel"></div></div><p>Vitae adipiscing turpis. Aenean ligula nibh in, molestie id viverra a, dapibus at dolor.</p></div>
  <div class="abs proj" style="left:377px;top:667px"><h3>Quisque cursus</h3><div class="frame"><div style="background:linear-gradient(#3f6fb0,#1f4f95)" role="img" aria-label="Single offshore turbine in open sea"></div></div><p>Vitae adipiscing turpis. Aenean ligula nibh in, molestie id viverra a, dapibus at dolor.</p></div>
</section>

<section class="abs invest">
  <div class="abs" style="left:18px;top:20px;width:64px;height:64px;border-radius:50%;background:var(--green)"></div>
  <h3 class="abs" style="left:104px;top:22px;font-weight:400;font-size:11.5px;color:#222">Invest in renewables projects. For as a long term money-earning</h3>
  <p class="abs" style="left:105px;top:43px;width:420px;font-size:8.6px;line-height:12.5px;color:#444">Ut dapibus ipsum ut molestie ullamcorper. Aenean eu metus ut lorem gravida viverra eget et lectus. Morbi condimentum efficitur ipsum at sagittis. Vestibulum ante ipsum primis in faucibus orci luctus et ultrices posuere cubilia Curae; Nam nec nisl diam.</p>
  <a class="abs btn btn-green" style="left:549px;top:30px;width:124px;height:51px;flex-direction:column;line-height:1">
    <span style="font-size:22px;font-weight:300">Join</span><span style="font-size:8px;margin-top:2px">With Us</span></a>
</section>

<footer>
  <div class="abs footer"></div>
  <div class="abs foot-h" style="left:38px">USEFUL LINKS</div>
  <ul class="abs links" style="left:40px;top:1033px"><li>Home</li><li>About Us</li><li>Service</li><li>FAQ</li><li>Sitemap</li><li>Contact Us</li></ul>

  <div class="abs foot-h" style="left:196px;font-weight:400">Workgrid</div>
  <span class="abs tile" style="left:306px;top:1016px"></span>
  <div class="abs feed">
    <div style="font-weight:700">Dale Warrick</div><div style="color:#888">CEO at Workgrid</div>
    <div style="margin-top:4px">“ Tunevale founder Ron Westfall w/ candid take on challenges of starting a company -- The Self-conscious Entrepreneur wgrd.in/KQ4mTx ”</div>
    <div style="margin-top:4px;margin-left:50px;font-weight:700">The Self-conscious Entrepreneur</div>
    <div style="margin-top:6px">Lena R. Ortiz It is always interesting to listen the things behind of the great...</div>
  </div>

  <div class="abs foot-h" style="left:382px;font-weight:400">Chirpnet</div>
  <span class="abs tile" style="left:522px;top:1016px;background:#2aa7a0"></span>
  <div class="abs tweet" style="top:1040px"><span class="bird"></span><div>@sam_ridley <em>Curabitur rhoncus lorem a tortor luctus mollis non bibendum nisl. Pellentesque eros massa.</em><br><span class="when">2 days ago</span></div></div>
  <div class="abs tweet" style="top:1095px"><span class="bird"></span><div><em>Lorem rhoncus lorem a tortor luctus mollis non bibendum nisl. Pellentesque eros</em> http://lorem/ipsum<br>3 days ago</div></div>

  <div class="abs foot-h" style="left:598px">CONTACT</div>
  <p class="abs" style="left:599px;top:1034px;width:140px;font-size:7.6px;line-height:10px;color:#777">Doloreiur quia commolu ptatemp dolupta oreprerum</p>
  <div class="abs field" style="top:1067px">Email</div>
  <div class="abs field" style="top:1093px">Contact For <span style="float:right;margin-right:8px">&#8964;</span></div>
  <a class="abs btn btn-green" style="left:685px;top:1123px;width:53px;height:15px;font-size:8px;box-shadow:none">CONTACT</a>

  <div class="abs bottom"></div>
  <div class="abs brand" style="left:39px;top:1169px;gap:6px"><span class="brand-dot" style="width:21px;height:21px;background:var(--white)"></span><span class="brand-name" style="font-size:19px;color:var(--white)">Bellmoran</span></div>
  <div class="abs" style="left:607px;top:1175px;font-size:8.2px;color:var(--white)">© 2015 yoursite. All rights reserved.</div>
</footer>
</body>
</html>
```